Fire Risk Assessment App needs a sleek UI design

I need a sleek, modern but professional design for my 5 page Fire Risk Assessment App. Include gradient background, fire themed colours including reds, yellows, light orange and a touch of black. Design must ooze simplicity and professionalism. This is for the UK market. See attached images and word doc for more information.

Target Market(s)

General public and business owners

Industry/Entity Type

Technology / Fire Safety

Colors
00AB8E
00BBA5
67D7C9
C6EFE9
E9F9F6
59FF00
82FF00
B8FF75
E3FFCB
F4FFEA
FFC000
F8CF3A
FAE287
FDF2CF
FEFAEE
F0912C
F2A743
F7CA91
FBE8D2
FDF5EE
EE7325
F08F49
F5BC92
FAE3D3
FDF4ED
EB3D1F
EC4F4E
F09395
F8D3D4
FCEDEE

```html
<!DOCTYPE html>
<html lang="en">
<head>
<meta charset="utf-8">
<title>Fire Risk Assessment App – Screens</title>
<link href="https://fonts.googleapis.com/css2?family=Poppins:wght@400;500;600;700&display=swap" rel="stylesheet">
<style>
  :root{
    --board-a:#6d4033;
    --board-b:#5a3226;
    --cream:#fdf5ee;
    --white:#ffffff;
    --ink:#231815;
    --muted:#7d7470;
    --line:#efe6df;
    --red:#eb3d1f;
    --orange:#ee7325;
    --orange-2:#f08f49;
    --yellow:#ffc000;
    --green:#2bb24c;
    --teal:#00bba5;
    --pill:#f6ecec;
    --grad-warm:linear-gradient(170deg,#f5b335 0%,#f08f2c 45%,#ee7325 75%,#e9552a 100%);
    --grad-btn:linear-gradient(90deg,#ee7325,#eb3d1f);
  }
  *{box-sizing:border-box;margin:0;padding:0}
  html,body{width:1200px;height:1200px;overflow:hidden}
  body{font-family:"Poppins",sans-serif;color:var(--ink);background:var(--board-b);-webkit-font-smoothing:antialiased;text-rendering:geometricPrecision}
  .board{position:absolute;left:0;top:0;width:1932px;height:1932px;zoom:0.621118;
    background:radial-gradient(circle at 30% 20%,var(--board-a),var(--board-b) 80%)}
  .abs{position:absolute}

  .brand-word{position:absolute;left:556px;top:124px;font-size:28px;font-weight:600;color:var(--orange-2)}
  .headline{position:absolute;left:705px;top:110px;font-size:54px;font-weight:500;color:#fff;letter-spacing:1.5px;white-space:nowrap}

  .screen-label{position:absolute;width:12px;writing-mode:vertical-rl;transform:rotate(180deg);
    font-size:9px;letter-spacing:5px;color:#e8d9d2;font-weight:500;white-space:nowrap}

  .screen{position:absolute;width:205px;height:446px;border-radius:24px;overflow:hidden;background:var(--cream);white-space:nowrap}
  .screen.tall{height:694px}
  .status{position:absolute;left:26px;top:8px;right:18px;display:flex;justify-content:space-between;align-items:center;font-size:8.5px;font-weight:500}
  .status .sig{display:flex;gap:3px;align-items:center}
  .status .sig i{display:block;width:10px;height:5px;border-radius:1.5px;background:currentColor}
  .status .sig b{display:block;width:6px;height:5px;border-radius:3px 3px 0 0;background:currentColor}
  .home-bar{position:absolute;left:50%;bottom:8px;width:78px;height:3px;border-radius:2px;background:#1c1c1c;transform:translateX(-50%)}
  .on-warm{color:#fff}
  .on-warm .home-bar{background:#fff}
  .warm{background:var(--grad-warm)}

  svg.ico{display:block;flex:none}
  .page-title{position:absolute;left:11px;top:33px;display:flex;align-items:center;gap:6px;font-size:10px;font-weight:600}
  .title-dot{width:13px;height:13px;border-radius:50%;background:var(--red);display:flex;align-items:center;justify-content:center}

  .btn{position:absolute;height:20px;border-radius:10px;display:flex;align-items:center;justify-content:center;gap:5px;font-size:7px;font-weight:600;white-space:nowrap}
  .btn-fill{background:var(--grad-btn);color:#fff}
  .btn-outline{border:1px solid var(--red);color:var(--red);background:#fff}

  .splash-flame{position:absolute;left:40px;top:200px;width:190px;height:230px;border-radius:50% 50% 0 0;
    background:radial-gradient(ellipse at 50% 70%,rgba(255,255,255,.16),rgba(255,255,255,0) 70%)}
  .splash-mark{position:absolute;left:0;right:0;top:88px;display:flex;flex-direction:column;align-items:center;gap:6px}
  .splash-mark span.c{width:40px;height:40px;border-radius:50%;background:#fff}
  .splash-mark span.n{font-size:11px;font-weight:600;color:#fff}
  .splash-tag{position:absolute;left:0;right:0;top:168px;text-align:center;font-size:8.5px;line-height:13px;color:#fff}
  .foot-note{position:absolute;left:0;right:0;bottom:28px;text-align:center;font-size:6.5px;color:#fff}

  .walk-brand{position:absolute;left:14px;top:46px;font-size:8px;font-weight:600;color:#fff}
  .walk-art{position:absolute;left:20px;top:62px;width:168px;height:228px;border-radius:8px;
    background:linear-gradient(160deg,rgba(255,255,255,.9),rgba(255,255,255,.75) 55%,rgba(235,61,31,.55))}
  .btn-login{left:16px;right:16px;top:338px;height:23px;border-radius:12px;background:#f97a1d;color:#fff}
  .btn-create{left:16px;right:16px;top:368px;height:23px;border-radius:12px;border:1px solid #fff;color:#fff}

  .card{position:absolute;background:#fff;border-radius:6px}
  .row-item{position:absolute;left:11px;right:11px;height:34px;background:#fff;border-radius:6px;display:flex;align-items:center;padding:0 8px;gap:7px}
  .row-item .t{display:block;font-size:7px;font-weight:500;line-height:10px}
  .row-item .s{display:block;font-size:5.5px;color:var(--muted)}
  .row-item .end{margin-left:auto}
  .ic{width:20px;height:20px;border-radius:50%;display:flex;align-items:center;justify-content:center;flex:none}
  .ic.yellow{background:var(--yellow)}
  .ic.teal{background:var(--teal)}
  .tick-ring{width:17px;height:17px;border-radius:50%;border:1.3px solid var(--green);display:flex;align-items:center;justify-content:center}
  .section-h{position:absolute;left:11px;font-size:9px;font-weight:500}
  .pill-link{position:absolute;left:53px;top:303px;height:15px;padding:0 9px;border-radius:8px;border:1px solid var(--red);color:var(--red);
    display:flex;align-items:center;gap:4px;font-size:6px;font-weight:600;white-space:nowrap}

  .nav{position:absolute;left:0;right:0;bottom:0;height:44px;background:linear-gradient(90deg,#e24722,#d6341c);display:flex;justify-content:space-around;padding:4px 6px 0}
  .nav a{display:flex;flex-direction:column;align-items:center;gap:2px;font-size:5px;color:#ffd7c9;text-decoration:none;width:32px}
  .nav a.on{color:#fff;font-weight:600}
  .nav .mid{width:14px;height:14px;border-radius:50%;background:var(--yellow);margin-top:2px}
  .nav .home-bar{background:#fff}

  .opt{position:absolute;left:11px;right:11px;height:40px;border-radius:6px;background:#fff;display:flex;align-items:center;gap:9px;padding:0 10px;font-size:7px;font-weight:500}
  .opt.sel{border:1.2px solid var(--red)}
  .radio{width:9px;height:9px;border-radius:50%;border:1px solid var(--red);display:flex;align-items:center;justify-content:center;flex:none}
  .radio.on::after{content:"";width:5px;height:5px;border-radius:50%;background:var(--red)}
  .opt .ic{width:24px;height:24px}

  .q-head{position:absolute;left:0;right:0;top:0;height:104px;background:var(--cream)}
  .q-body{position:absolute;left:0;right:0;top:104px;bottom:0;background:#fff}
  .q-kicker{position:absolute;left:11px;top:34px;font-size:5.5px;font-weight:600;letter-spacing:.2px}
  .q-title{position:absolute;left:11px;top:42px;font-size:13px;font-weight:700}
  .q-section{position:absolute;left:11px;top:63px;font-size:8px}
  .q-section b{font-weight:600}
  .q-save{position:absolute;right:8px;top:32px;width:56px;display:flex;flex-direction:column;align-items:center;gap:3px;font-size:5.5px;font-weight:500}
  .q-save span.c{width:23px;height:23px;border-radius:50%;border:1.2px solid var(--red);display:flex;align-items:center;justify-content:center;background:#fff}
  .q-badge{position:absolute;left:81px;top:90px;width:44px;height:44px;border-radius:50%;background:#fff;border:3px solid var(--green);display:flex;align-items:center;justify-content:center}
  .q-topic{position:absolute;left:0;right:0;top:140px;text-align:center}
  .q-topic .a{font-size:7.8px;font-weight:600}
  .q-topic .b{font-size:7px;color:var(--muted);margin-top:2px}
  .q-rule{position:absolute;left:11px;right:11px;top:172px;height:1px;background:var(--line)}
  .q-num{position:absolute;left:11px;top:183px;font-size:5.8px;font-weight:700;color:var(--red)}
  .q-text{position:absolute;left:11px;right:9px;top:195px;font-size:10.2px;line-height:15.5px;font-weight:500;white-space:normal}
  .answers{position:absolute;left:0;right:0;top:242px;display:flex;justify-content:space-between;padding:0 27px}
  .ans{display:flex;flex-direction:column;align-items:center;gap:5px;font-size:5.8px;width:24px}
  .ans .c{width:23px;height:23px;border-radius:50%;display:flex;align-items:center;justify-content:center;border:1.2px solid}
  .ans.yes .c{border-color:var(--green)}
  .ans.no .c{border-color:var(--red)}
  .ans.na .c{border-color:var(--orange)}
  .ans.yes.on .c{background:var(--green)}
  .ans.yes.on{color:var(--green);font-weight:600}
  .ans.no.on .c{background:var(--red)}
  .ans.no.on{color:var(--red);font-weight:600}
  .q-note{position:absolute;left:11px;right:11px;top:288px;height:24px;border:1px solid var(--line);border-radius:4px;font-size:5.8px;display:flex;align-items:center;padding-left:8px;font-weight:500}
  .more{position:absolute;left:11px;right:11px}
  .more .lbl{font-size:5.5px;color:var(--muted);font-weight:500;margin-bottom:8px}
  .more .btns{display:flex;gap:6px}
  .more .btns span{flex:1;height:20px;border-radius:3px;background:var(--pill);display:flex;align-items:center;gap:5px;padding-left:8px;font-size:6.5px}
  .photos-lbl{position:absolute;left:11px;top:378px;font-size:5.5px;color:var(--muted);font-weight:500}
  .photo{position:absolute;left:11px;right:11px;top:390px;height:184px;border-radius:4px;
    background:linear-gradient(150deg,#4a4d50,#8e9396 55%,#c9ccce)}
  .photo .del{position:absolute;right:7px;top:7px;width:14px;height:14px;border-radius:50%;background:#fff;display:flex;align-items:center;justify-content:center}
  .q-foot{position:absolute;left:0;right:0;bottom:0;height:88px;background:#fff;border-top:4px solid var(--cream)}
  .q-foot .lbl{position:absolute;left:11px;right:11px;top:8px;display:flex;justify-content:space-between;font-size:5px;font-weight:600}
  .q-foot .bar{position:absolute;left:11px;right:11px;top:19px;height:3px;border-radius:2px;background:var(--line)}
  .q-foot .bar i{display:block;width:60%;height:100%;border-radius:2px;background:var(--green)}
  .q-foot .btn{top:34px;width:87px}
  .q-foot .prev{left:11px}
  .q-foot .next{right:11px}

  .sub{position:absolute;left:11px;top:74px;font-size:6.8px}
  .plan{position:absolute;left:11px;right:11px;height:38px;border-radius:6px;background:#fff;display:flex;align-items:center;padding:0 9px;gap:9px}
  .plan.sel{border:1.2px solid var(--red)}
  .plan .tier{display:inline-block;font-size:5px;font-weight:600;padding:1.5px 5px;border-radius:6px;margin-bottom:3px}
  .plan .nm{display:block;font-size:6.5px;font-weight:500}
  .plan .price{margin-left:auto;text-align:right;font-size:7.5px;font-weight:600;color:var(--red);line-height:9px}
  .plan .price s{display:block;color:var(--muted);font-weight:500;font-size:7px}
  .plan .tag{position:absolute;right:36px;top:-5px;font-size:4.8px;font-weight:700;padding:1.5px 10px;border-radius:3px 3px 0 0;color:#fff;background:var(--red)}
  .plan .tag.best{background:var(--yellow);color:var(--ink)}
  .tier.bronze{background:#9a4b23;color:#fff}
  .tier.silver{background:#e2e2e2}
  .tier.gold{background:var(--yellow);color:#fff}
  .tier.plat{background:#ececec}

  .compose{position:absolute;left:0;right:0;top:92px;bottom:44px;background:#fff}
  .compose .ph{position:absolute;left:11px;top:10px;font-size:6.5px;color:var(--muted)}
  .compose .mic{position:absolute;right:11px;top:6px;width:15px;height:15px;border-radius:50%;background:#fff;box-shadow:0 0 0 1px var(--line);display:flex;align-items:center;justify-content:center}
</style>
</head>
<body>
<svg width="0" height="0" style="position:absolute">
  <defs>
    <symbol id="i-tick" viewBox="0 0 24 24"><path d="M5 12.5l4.5 4.5L19 7.5" fill="none" stroke="currentColor" stroke-width="2.6" stroke-linecap="round" stroke-linejoin="round"/></symbol>
    <symbol id="i-x" viewBox="0 0 24 24"><path d="M7 7l10 10M17 7L7 17" fill="none" stroke="currentColor" stroke-width="2.6" stroke-linecap="round"/></symbol>
    <symbol id="i-na" viewBox="0 0 24 24"><circle cx="12" cy="12" r="7" fill="none" stroke="currentColor" stroke-width="2.2"/><path d="M7 17L17 7" stroke="currentColor" stroke-width="2.2"/></symbol>
    <symbol id="i-mic" viewBox="0 0 24 24"><rect x="9" y="3" width="6" height="11" rx="3" fill="currentColor"/><path d="M6 11a6 6 0 0012 0M12 17v4" fill="none" stroke="currentColor" stroke-width="2"/></symbol>
    <symbol id="i-cam" viewBox="0 0 24 24"><path d="M3 8h4l2-3h6l2 3h4v12H3z" fill="currentColor"/><circle cx="12" cy="13" r="3.5" fill="#fff"/></symbol>
    <symbol id="i-left" viewBox="0 0 24 24"><path d="M19 12H5M11 6l-6 6 6 6" fill="none" stroke="currentColor" stroke-width="2.4" stroke-linecap="round" stroke-linejoin="round"/></symbol>
    <symbol id="i-right" viewBox="0 0 24 24"><path d="M5 12h14M13 6l6 6-6 6" fill="none" stroke="currentColor" stroke-width="2.4" stroke-linecap="round" stroke-linejoin="round"/></symbol>
    <symbol id="i-bolt" viewBox="0 0 24 24"><path d="M13.5 2L5 13.5h6L9.5 22 19 9.5h-6.2z" fill="#ffc000" stroke="#f0912c" stroke-width="1"/></symbol>
    <symbol id="i-save" viewBox="0 0 24 24"><path d="M5 4h11l3 3v13H5z" fill="#eb3d1f"/><rect x="8" y="5" width="7" height="4" fill="#fff"/><rect x="8" y="13" width="8" height="5" fill="#fff"/></symbol>
    <symbol id="i-house" viewBox="0 0 24 24"><path d="M4 11l8-6 8 6v9H4z" fill="#fff"/><rect x="10" y="14" width="4" height="6" fill="#ffc000"/></symbol>
    <symbol id="i-building" viewBox="0 0 24 24"><path d="M5 4h9v16H5zM14 9h5v11h-5z" fill="#fff"/><path d="M7 7h2v2H7zM10 7h2v2h-2zM7 11h2v2H7zM10 11h2v2h-2z" fill="#00bba5"/></symbol>
    <symbol id="i-gauge" viewBox="0 0 24 24"><circle cx="12" cy="12" r="8" fill="none" stroke="currentColor" stroke-width="2.2"/><path d="M12 12l4-4" stroke="currentColor" stroke-width="2.2" stroke-linecap="round"/></symbol>
    <symbol id="i-card" viewBox="0 0 24 24"><rect x="3" y="5" width="18" height="14" rx="2" fill="none" stroke="currentColor" stroke-width="2"/><path d="M3 10h18" stroke="currentColor" stroke-width="2"/></symbol>
    <symbol id="i-help" viewBox="0 0 24 24"><circle cx="12" cy="12" r="9" fill="none" stroke="currentColor" stroke-width="2"/><path d="M9.5 9.5a2.5 2.5 0 115 0c0 1.8-2.5 2-2.5 4M12 16.5v.5" fill="none" stroke="currentColor" stroke-width="2" stroke-linecap="round"/></symbol>
    <symbol id="i-logout" viewBox="0 0 24 24"><rect x="5" y="3" width="14" height="18" rx="1.5" fill="none" stroke="currentColor" stroke-width="2"/><path d="M9 12h6M12 9l3 3-3 3" fill="none" stroke="currentColor" stroke-width="2" stroke-linecap="round"/></symbol>
    <symbol id="i-user" viewBox="0 0 24 24"><circle cx="12" cy="12" r="10" fill="currentColor"/><circle cx="12" cy="9.5" r="3.5" fill="#fdf5ee"/><path d="M6 18a7 5 0 0112 0" fill="#fdf5ee"/></symbol>
    <symbol id="i-user-add" viewBox="0 0 24 24"><circle cx="10" cy="8" r="4" fill="currentColor"/><path d="M3 20a7 6 0 0114 0z" fill="currentColor"/><path d="M19 8v6M16 11h6" stroke="currentColor" stroke-width="2"/></symbol>
    <symbol id="i-send" viewBox="0 0 24 24"><path d="M3 4l18 8-18 8 3-8z" fill="currentColor"/></symbol>
    <symbol id="i-trash" viewBox="0 0 24 24"><path d="M6 7h12l-1 14H7zM4 5h16M9 5V3h6v2" fill="#eb3d1f"/></symbol>
    <symbol id="i-plus" viewBox="0 0 24 24"><path d="M12 6v12M6 12h12" stroke="#fff" stroke-width="3" stroke-linecap="round"/></symbol>
    <symbol id="i-flame" viewBox="0 0 24 24"><circle cx="12" cy="13" r="6" fill="currentColor"/></symbol>
  </defs>
</svg>

<main class="board">
  <div class="brand-word">Emberline</div>
  <h1 class="headline">Fire Risk Assessment App</h1>

  <div class="screen-label" style="left:407px;top:256px">SPLASH SCREEN</div>
  <section class="screen warm on-warm" style="left:432px;top:256px">
    <div class="status"><span>9:41</span><span class="sig"><i></i><i></i><b></b></span></div>
    <div class="splash-flame" role="img" aria-label="Large faint flame motif in lighter orange tones"></div>
    <div class="splash-mark"><span class="c"></span><span class="n">Emberline</span></div>
    <p class="splash-tag">The most user friendly<br><b>Fire Risk Assessment</b> available</p>
    <p class="foot-note">Created and endorsed by British Firefighters</p>
    <div class="home-bar"></div>
  </section>

  <div class="screen-label" style="left:703px;top:256px">WALKTHROUGH SCREEN</div>
  <section class="screen warm on-warm" style="left:728px;top:256px">
    <div class="status"><span>9:41</span><span class="sig"><i></i><i></i><b></b></span></div>
    <div class="walk-brand">Emberline</div>
    <div class="walk-art" role="img" aria-label="Illustration of stacked assessment question cards with a tapping hand"></div>
    <div class="btn btn-login"><svg class="ico" width="9" height="9"><use href="#i-user-add"/></svg>Customer log in</div>
    <div class="btn btn-create"><svg class="ico" width="9" height="9"><use href="#i-user-add"/></svg>Create a free account</div>
    <p class="foot-note">Quick tap responses and voice activated typing.</p>
    <div class="home-bar"></div>
  </section>

  <div class="screen-label" style="left:999px;top:256px">DASHBOARD DESIGN ALT 1</div>
  <section class="screen" style="left:1024px;top:256px">
    <div class="status"><span>9:41</span><span class="sig"><i></i><i></i><b></b></span></div>
    <div class="page-title"><span class="title-dot"><svg class="ico" width="9" height="9" style="color:#fff"><use href="#i-gauge"/></svg></span>Dashboard</div>
    <svg class="ico abs" width="13" height="13" style="right:11px;top:34px"><use href="#i-user"/></svg>
    <div class="card" style="left:11px;right:11px;top:60px;height:114px">
      <div class="abs" style="left:8px;top:8px;font-size:6.5px;font-weight:500">Fire Risk Assessments</div>
      <div class="abs" style="right:8px;top:8px;font-size:5.5px;font-weight:700;color:var(--red)">VIEW ALL</div>
      <div class="abs" style="left:6px;right:6px;top:22px;height:36px;border-radius:6px;box-shadow:0 0 0 1px var(--line);display:flex;align-items:center;gap:7px;padding:0 8px">
        <span class="ic yellow" style="width:22px;height:22px"><svg class="ico" width="13" height="13"><use href="#i-house"/></svg></span>
        <span><span style="display:block;font-size:7px;font-weight:500">Hartwell Residence</span><span style="display:block;font-size:4.8px;font-weight:700;color:var(--red)">● IN-PROGRESS</span></span>
        <svg class="ico" width="20" height="20" viewBox="0 0 24 24" style="margin-left:auto"><circle cx="12" cy="12" r="9.5" fill="none" stroke="#eee" stroke-width="2.5"/><circle cx="12" cy="12" r="9.5" fill="none" stroke="#2bb24c" stroke-width="2.5" stroke-dasharray="44.8 60" transform="rotate(-90 12 12)"/><text x="12" y="14" font-size="5" text-anchor="middle" font-family="Poppins" font-weight="600">75%</text></svg>
      </div>
      <div class="abs" style="left:75px;top:68px;display:flex;gap:3px"><i style="width:14px;height:2.5px;border-radius:2px;background:var(--red)"></i><i style="width:4px;height:2.5px;border-radius:2px;background:#f3d6cc"></i><i style="width:4px;height:2.5px;border-radius:2px;background:#f3d6cc"></i><i style="width:4px;height:2.5px;border-radius:2px;background:#f3d6cc"></i></div>
      <div class="btn btn-fill" style="left:8px;right:8px;top:84px"><svg class="ico" width="8" height="8" style="color:#fff"><use href="#i-flame"/></svg>Add new assessment</div>
    </div>
    <div class="section-h" style="top:196px">Completed Assessments</div>
    <div class="row-item" style="top:216px"><span class="ic teal"><svg class="ico" width="12" height="12"><use href="#i-building"/></svg></span><span><span class="t">Elmcroft Nursing Home</span><span class="s">18 Jul 2024</span></span><span class="end tick-ring"><svg class="ico" width="10" height="10" style="color:var(--green)"><use href="#i-tick"/></svg></span></div>
    <div class="row-item" style="top:256px"><span class="ic yellow"><svg class="ico" width="12" height="12"><use href="#i-house"/></svg></span><span><span class="t">The Linden Residences</span><span class="s">10 Jul 2024</span></span><span class="end tick-ring"><svg class="ico" width="10" height="10" style="color:var(--green)"><use href="#i-tick"/></svg></span></div>
    <div class="pill-link">View all completed <svg class="ico" width="7" height="7"><use href="#i-right"/></svg></div>
    <div class="section-h" style="top:340px">Purchase History</div>
    <div class="abs" style="left:11px;top:362px;display:flex;gap:7px;align-items:center">
      <span class="ic teal" style="width:14px;height:14px"><svg class="ico" width="9" height="9"><use href="#i-building"/></svg></span>
      <span><span style="display:block;font-size:6.5px;font-weight:500">Commercial Fire Risk Assessments</span><span style="display:block;font-size:5.2px;color:var(--muted)">Sat, 6 July 2024 • 10:48:57</span></span>
    </div>
    <nav class="nav">
      <a class="on"><svg class="ico" width="10" height="10"><use href="#i-gauge"/></svg>Dashboard</a>
      <a><svg class="ico" width="10" height="10"><use href="#i-card"/></svg>Purchases</a>
      <a><span class="mid"></span></a>
      <a><svg class="ico" width="10" height="10"><use href="#i-help"/></svg>Support</a>
      <a><svg class="ico" width="10" height="10"><use href="#i-logout"/></svg>Logout</a>
      <div class="home-bar"></div>
    </nav>
  </section>

  <div class="screen-label" style="left:1295px;top:256px">ADD NEW ASSESSMENT</div>
  <section class="screen" style="left:1320px;top:256px">
    <div class="status"><span>9:41</span><span class="sig"><i></i><i></i><b></b></span></div>
    <div class="page-title"><span class="title-dot"><svg class="ico" width="9" height="9"><use href="#i-plus"/></svg></span>Add Fire Risk Assessment</div>
    <div class="sub" style="top:67px">Select type of property</div>
    <div class="opt sel" style="top:92px"><span class="radio on"></span><span class="ic yellow"><svg class="ico" width="14" height="14"><use href="#i-house"/></svg></span>Residential</div>
    <div class="opt" style="top:138px"><span class="radio"></span><span class="ic teal"><svg class="ico" width="14" height="14"><use href="#i-building"/></svg></span>Commercial</div>
    <div class="btn btn-outline" style="left:11px;width:87px;top:392px;background:transparent">Cancel</div>
    <div class="btn btn-fill" style="right:11px;width:87px;top:392px">Continue</div>
    <div class="home-bar"></div>
  </section>

  <div class="screen-label" style="left:407px;top:786px">ADD ASSESSMENT - QUESTION</div>
  <section class="screen" style="left:432px;top:786px">
    <div class="q-head"></div><div class="q-body"></div>
    <div class="status"><span>9:41</span><span class="sig"><i></i><i></i><b></b></span></div>
    <div class="q-kicker">FIRE RISK ASSESSMENT</div><div class="q-title">Fire Hazards</div><div class="q-section"><b>Section 22.5</b> / 30.00</div>
    <div class="q-save"><span class="c"><svg class="ico" width="11" height="11"><use href="#i-save"/></svg></span>Save and close</div>
    <div class="q-badge"><svg class="ico" width="24" height="24"><use href="#i-bolt"/></svg></div>
    <div class="q-topic"><div class="a">Electronic Sources of Ignition</div><div class="b">(Clause 13 &amp; Annex B)</div></div>
    <div class="q-rule"></div><div class="q-num">QUESTION 22.05</div>
    <p class="q-text">Are reasonable measures taken to prevent fires of electrical origin?</p>
    <div class="answers">
      <div class="ans yes"><span class="c"><svg class="ico" width="13" height="13" style="color:var(--green)"><use href="#i-tick"/></svg></span>Yes</div>
      <div class="ans no"><span class="c"><svg class="ico" width="13" height="13" style="color:var(--red)"><use href="#i-x"/></svg></span>No</div>
      <div class="ans na"><span class="c"><svg class="ico" width="13" height="13" style="color:var(--orange)"><use href="#i-na"/></svg></span>N/A</div>
    </div>
    <div class="more" style="top:294px"><div class="lbl">MORE OPTIONS</div><div class="btns"><span><svg class="ico" width="8" height="8"><use href="#i-mic"/></svg>Mic</span><span><svg class="ico" width="8" height="8"><use href="#i-cam"/></svg>Take a photo</span></div></div>
    <div class="q-foot"><div class="lbl"><span>ASSESSMENT PROGRESS</span><span>60%</span></div><div class="bar"><i></i></div>
      <div class="btn btn-outline prev"><svg class="ico" width="7" height="7"><use href="#i-left"/></svg>Prev</div>
      <div class="btn btn-fill next">Next<svg class="ico" width="7" height="7"><use href="#i-right"/></svg></div>
      <div class="home-bar"></div></div>
  </section>

  <div class="screen-label" style="left:703px;top:786px">ADD ASSESSMENT - QUESTION - YES</div>
  <section class="screen" style="left:728px;top:786px">
    <div class="q-head"></div><div class="q-body"></div>
    <div class="status"><span>9:41</span><span class="sig"><i></i><i></i><b></b></span></div>
    <div class="q-kicker">FIRE RISK ASSESSMENT</div><div class="q-title">Fire Hazards</div><div class="q-section"><b>Section 22.5</b> / 30.00</div>
    <div class="q-save"><span class="c"><svg class="ico" width="11" height="11"><use href="#i-save"/></svg></span>Save and close</div>
    <div class="q-badge"><svg class="ico" width="24" height="24"><use href="#i-bolt"/></svg></div>
    <div class="q-topic"><div class="a">Electronic Sources of Ignition</div><div class="b">(Clause 13 &amp; Annex B)</div></div>
    <div class="q-rule"></div><div class="q-num">QUESTION 22.05</div>
    <p class="q-text">Are reasonable measures taken to prevent fires of electrical origin?</p>
    <div class="answers">
      <div class="ans yes on"><span class="c"><svg class="ico" width="13" height="13" style="color:#fff"><use href="#i-tick"/></svg></span>Yes</div>
      <div class="ans no"><span class="c"><svg class="ico" width="13" height="13" style="color:var(--red)"><use href="#i-x"/></svg></span>No</div>
      <div class="ans na"><span class="c"><svg class="ico" width="13" height="13" style="color:var(--orange)"><use href="#i-na"/></svg></span>N/A</div>
    </div>
    <div class="more" style="top:294px"><div class="lbl">MORE OPTIONS</div><div class="btns"><span><svg class="ico" width="8" height="8"><use href="#i-mic"/></svg>Mic</span><span><svg class="ico" width="8" height="8"><use href="#i-cam"/></svg>Take a photo</span></div></div>
    <div class="q-foot"><div class="lbl"><span>ASSESSMENT PROGRESS</span><span>60%</span></div><div class="bar"><i></i></div>
      <div class="btn btn-outline prev"><svg class="ico" width="7" height="7"><use href="#i-left"/></svg>Prev</div>
      <div class="btn btn-fill next">Next<svg class="ico" width="7" height="7"><use href="#i-right"/></svg></div>
      <div class="home-bar"></div></div>
  </section>

  <div class="screen-label" style="left:999px;top:786px">ADD ASSESSMENT - QUESTION - NO</div>
  <section class="screen" style="left:1024px;top:786px">
    <div class="q-head"></div><div class="q-body"></div>
    <div class="status"><span>9:41</span><span class="sig"><i></i><i></i><b></b></span></div>
    <div class="q-kicker">FIRE RISK ASSESSMENT</div><div class="q-title">Fire Hazards</div><div class="q-section"><b>Section 22.5</b> / 30.00</div>
    <div class="q-save"><span class="c"><svg class="ico" width="11" height="11"><use href="#i-save"/></svg></span>Save and close</div>
    <div class="q-badge"><svg class="ico" width="24" height="24"><use href="#i-bolt"/></svg></div>
    <div class="q-topic"><div class="a">Electronic Sources of Ignition</div><div class="b">(Clause 13 &amp; Annex B)</div></div>
    <div class="q-rule"></div><div class="q-num">QUESTION 22.05</div>
    <p class="q-text">Are reasonable measures taken to prevent fires of electrical origin?</p>
    <div class="answers">
      <div class="ans yes"><span class="c"><svg class="ico" width="13" height="13" style="color:var(--green)"><use href="#i-tick"/></svg></span>Yes</div>
      <div class="ans no on"><span class="c"><svg class="ico" width="13" height="13" style="color:#fff"><use href="#i-x"/></svg></span>No</div>
      <div class="ans na"><span class="c"><svg class="ico" width="13" height="13" style="color:var(--orange)"><use href="#i-na"/></svg></span>N/A</div>
    </div>
    <div class="q-note">No, electric sockets are overloaded.</div>
    <div class="more" style="top:323px"><div class="lbl">MORE OPTIONS</div><div class="btns"><span><svg class="ico" width="8" height="8"><use href="#i-mic"/></svg>Mic</span><span><svg class="ico" width="8" height="8"><use href="#i-cam"/></svg>Take a photo</span></div></div>
    <div class="q-foot"><div class="lbl"><span>ASSESSMENT PROGRESS</span><span>60%</span></div><div class="bar"><i></i></div>
      <div class="btn btn-outline prev"><svg class="ico" width="7" height="7"><use href="#i-left"/></svg>Prev</div>
      <div class="btn btn-fill next">Next<svg class="ico" width="7" height="7"><use href="#i-right"/></svg></div>
      <div class="home-bar"></div></div>
  </section>

  <div class="screen-label" style="left:1295px;top:786px">ADD ASSESSMENT - QUESTION - ADD PHOTO</div>
  <section class="screen tall" style="left:1320px;top:786px">
    <div class="q-head"></div><div class="q-body"></div>
    <div class="status"><span>9:41</span><span class="sig"><i></i><i></i><b></b></span></div>
    <div class="q-kicker">FIRE RISK ASSESSMENT</div><div class="q-title">Fire Hazards</div><div class="q-section"><b>Section 22.5</b> / 30.00</div>
    <div class="q-save"><span class="c"><svg class="ico" width="11" height="11"><use href="#i-save"/></svg></span>Save and close</div>
    <div class="q-badge"><svg class="ico" width="24" height="24"><use href="#i-bolt"/></svg></div>
    <div class="q-topic"><div class="a">Electronic Sources of Ignition</div><div class="b">(Clause 13 &amp; Annex B)</div></div>
    <div class="q-rule"></div><div class="q-num">QUESTION 22.05</div>
    <p class="q-text">Are reasonable measures taken to prevent fires of electrical origin?</p>
    <div class="answers">
      <div class="ans yes"><span class="c"><svg class="ico" width="13" height="13" style="color:var(--green)"><use href="#i-tick"/></svg></span>Yes</div>
      <div class="ans no on"><span class="c"><svg class="ico" width="13" height="13" style="color:#fff"><use href="#i-x"/></svg></span>No</div>
      <div class="ans na"><span class="c"><svg class="ico" width="13" height="13" style="color:var(--orange)"><use href="#i-na"/></svg></span>N/A</div>
    </div>
    <div class="q-note">No, electric sockets are overloaded.</div>
    <div class="more" style="top:323px"><div class="lbl">MORE OPTIONS</div><div class="btns"><span><svg class="ico" width="8" height="8"><use href="#i-mic"/></svg>Mic</span><span><svg class="ico" width="8" height="8"><use href="#i-cam"/></svg>Take a photo</span></div></div>
    <div class="photos-lbl">PHOTOS</div>
    <div class="photo" role="img" aria-label="Photo of an overloaded extension lead with tangled cables on a floor"><span class="del"><svg class="ico" width="8" height="8"><use href="#i-trash"/></svg></span></div>
    <div class="q-foot"><div class="lbl"><span>ASSESSMENT PROGRESS</span><span>60%</span></div><div class="bar"><i></i></div>
      <div class="btn btn-outline prev"><svg class="ico" width="7" height="7"><use href="#i-left"/></svg>Prev</div>
      <div class="btn btn-fill next">Next<svg class="ico" width="7" height="7"><use href="#i-right"/></svg></div>
      <div class="home-bar"></div></div>
  </section>

  <div class="screen-label" style="left:407px;top:1316px">PURCHASE OPTIONS</div>
  <section class="screen" style="left:432px;top:1316px">
    <div class="status"><span>9:41</span><span class="sig"><i></i><i></i><b></b></span></div>
    <div class="page-title"><svg class="ico" width="16" height="16" style="color:var(--red)"><use href="#i-card"/></svg>Purchase Options</div>
    <div class="sub">Select Fire Risk Assessment Payment Options</div>
    <div class="plan" style="top:94px"><span class="radio"></span><span><span class="tier bronze">BRONZE 1</span><span class="nm">Fire Risk Assessment</span></span><span class="price">£19.99</span></div>
    <div class="plan sel" style="top:141px"><span class="tag best">BEST PRICE</span><span class="radio on"></span><span><span class="tier silver">SILVER 3</span><span class="nm">Fire Risk Assessment</span></span><span class="price"><s>£59.97</s>£54.99</span></div>
    <div class="plan" style="top:188px"><span class="tag">SAVE 20%</span><span class="radio"></span><span><span class="tier gold">GOLD 5</span><span class="nm">Fire Risk Assessment</span></span><span class="price"><s>£99.95</s>£89.99</span></div>
    <div class="plan" style="top:235px"><span class="tag">SAVE 30%</span><span class="radio"></span><span><span class="tier plat">PLATINUM 10</span><span class="nm">Fire Risk Assessment</span></span><span class="price"><s>£199.90</s>£174.99</span></div>
    <div class="btn btn-fill" style="left:11px;right:11px;top:334px;height:22px">Continue</div>
    <div class="btn btn-outline" style="left:11px;right:11px;top:363px;height:22px">Cancel</div>
    <nav class="nav">
      <a><svg class="ico" width="10" height="10"><use href="#i-gauge"/></svg>Dashboard</a>
      <a class="on"><svg class="ico" width="10" height="10"><use href="#i-card"/></svg>Purchases</a>
      <a><span class="mid"></span></a>
      <a><svg class="ico" width="10" height="10"><use href="#i-help"/></svg>Support</a>
      <a><svg class="ico" width="10" height="10"><use href="#i-logout"/></svg>Logout</a>
      <div class="home-bar"></div>
    </nav>
  </section>

  <div class="screen-label" style="left:703px;top:1316px">SUPPORT SCREEN</div>
  <section class="screen" style="left:728px;top:1316px">
    <div class="status"><span>9:41</span><span class="sig"><i></i><i></i><b></b></span></div>
    <div class="page-title"><span class="title-dot"><svg class="ico" width="9" height="9" style="color:#fff"><use href="#i-help"/></svg></span>Technical Support</div>
    <div class="sub">Our email support is open 24/7.</div>
    <div class="compose">
      <span class="ph">Type or record your concerns here</span>
      <span class="mic"><svg class="ico" width="7" height="7" style="color:var(--red)"><use href="#i-mic"/></svg></span>
      <div class="btn btn-fill" style="left:12px;right:12px;top:264px;height:22px"><svg class="ico" width="8" height="8" style="color:#fff"><use href="#i-send"/></svg>Send</div>
    </div>
    <nav class="nav">
      <a><svg class="ico" width="10" height="10"><use href="#i-gauge"/></svg>Dashboard</a>
      <a><svg class="ico" width="10" height="10"><use href="#i-card"/></svg>Purchases</a>
      <a><span class="mid"></span></a>
      <a class="on"><svg class="ico" width="10" height="10"><use href="#i-help"/></svg>Support</a>
      <a><svg class="ico" width="10" height="10"><use href="#i-logout"/></svg>Logout</a>
      <div class="home-bar"></div>
    </nav>
  </section>
</main>
</body>
</html>
```